Purrline Fest Ticket Card Design

We’re looking to create a complimentary “ticket” card for Purrline Fest that can be handed out physically. We host an event for cat lovers. The card should feel special and collectible. Size will be a standard business card (3.5" x 2") Orientation is open to designer recommendation. This ticket will be used as a complimentary entry pass for select guests, partners, & giveaways. Key elements to Include are the Purrline Fest logo (provided), the words “Complimentary Ticket” or similar wording (open to creative phrasing and cat puns) A blank space for the Event date (to be written in) & Ticket number (to be written in) . Event Name is always "Purrline Bazaar & Rescue Gala". We want the ticket to feel clean & modern but slightly playful with a cat-inspired touch (think clever, not kitschy). Could include a subtle cat motif or texture (e.g., whisker lines, paw detail, soft patterning) Open to unique layout ideas that still leave clear writing space. Avoid overcrowding of elements. Ticket should also have fine print "This ticket is not redeemable for cash and cannot be combined with any other offers or discounts, can only be used for the date indicated"

Target Market(s)

Women

Industry/Entity Type

pets

Colors
6B429C
8869AF
B7A5CE
E3DAEB
F3F0F8

Requirements
Must have
• Purrline Fest Logo & words around complimentary ticket as well as the fine print
Nice to have
• cat-inspired touch (think clever, not kitschy). Could include a subtle cat motif or texture (e.g., whisker lines, paw detail, soft patterning)
Should not have
• should not look cartoony

```html
<!DOCTYPE html>
<html lang="en">
<head>
<meta charset="utf-8">
<title>Purrline Fest – Complimentary Ticket</title>
<link rel="stylesheet" href="https://fonts.googleapis.com/css2?family=Montserrat:wght@400;700&family=Cookie&family=Roboto+Condensed:wght@400&display=swap">
<style>
  :root {
    --page-bg: #ffffff;
    --ink: #111111;
    --card-top: #2f2c3d;
    --card-bottom: #232130;
    --lilac-pale: #f3f0f8;
    --lilac-light: #e3dacf;
    --lilac-soft: #e3daeb;
    --lilac-mid: #b7a5ce;
    --violet: #8869af;
    --violet-deep: #6b429c;
    --silver: #d9d9de;
  }
  * { box-sizing: border-box; margin: 0; padding: 0; }
  html, body {
    width: 1200px; height: 1200px; overflow: hidden;
    background: var(--page-bg);
  }
  .stage { position: relative; width: 1200px; height: 1200px; }

  .brand-mark {
    position: absolute; left: 0; top: 150px; width: 1200px;
    text-align: center;
  }
  .brand-name {
    font-family: "Montserrat", sans-serif; font-weight: 700;
    font-size: 96px; line-height: 1.02; color: var(--ink);
    letter-spacing: 1px;
  }

  .ticket {
    position: absolute; left: 124px; top: 427px;
    width: 960px; height: 552px; border-radius: 26px;
    background: linear-gradient(180deg, var(--card-top), var(--card-bottom));
    overflow: hidden;
  }
  .motif {
    position: absolute; top: 0; height: 100%; width: 240px;
  }
  .motif-left {
    left: 0;
    background: radial-gradient(ellipse at 30% 45%, rgba(183,165,206,0.08), rgba(183,165,206,0) 70%);
  }
  .motif-right {
    right: 0;
    background: radial-gradient(ellipse at 70% 45%, rgba(183,165,206,0.08), rgba(183,165,206,0) 70%);
  }

  .ticket-brand {
    position: absolute; left: 0; top: 110px; width: 100%;
    text-align: center;
    font-family: "Montserrat", sans-serif; font-weight: 700;
    font-size: 78px; line-height: 1.05; color: var(--lilac-soft);
    letter-spacing: 1px;
  }

  .entry-title {
    position: absolute; right: 396px; top: 346px;
    text-align: right;
    font-family: "Cookie", cursive; color: var(--violet);
    font-size: 50px; line-height: 52px;
  }
  .divider {
    position: absolute; left: 580px; top: 342px;
    width: 2px; height: 162px; background: var(--silver);
  }
  .write-in {
    position: absolute; left: 596px; width: 327px;
    font-family: "Roboto Condensed", sans-serif;
    font-size: 22px; color: var(--silver); letter-spacing: 0.3px;
    padding-bottom: 8px; border-bottom: 2px solid var(--silver);
  }
  .write-in.event-date { top: 370px; }
  .write-in.ticket-no { top: 436px; }

  .fine-print {
    position: absolute; left: 0; bottom: 24px; width: 100%;
    text-align: center;
    font-family: "Roboto Condensed", sans-serif;
    font-size: 15px; color: var(--violet);
  }
</style>
</head>
<body>
<main class="stage">
  <header class="brand-mark">
    <p class="brand-name">Purrline<br>Fest</p>
  </header>

  <section class="ticket">
    <div class="motif motif-left" role="img" aria-label="Subtle embossed paw prints and whisker lines"></div>
    <div class="motif motif-right" role="img" aria-label="Subtle embossed paw prints and whisker lines"></div>

    <p class="ticket-brand">Purrline<br>Fest</p>

    <p class="entry-title">One Purrfect Entry<br>(Complimentary Ticket)</p>

    <div class="divider"></div>
    <p class="write-in event-date">EVENT DATE:</p>
    <p class="write-in ticket-no">TICKET NO:</p>

    <p class="fine-print">This ticket is not redeemable for cash and cannot be combined with any other offers or discounts, can only be used for the date indicated.</p>
  </section>
</main>
</body>
</html>
```